Hispanic Financial Counseling and Advocate Firm seeks business card design

Looking for a clean, professional business card design. This is a firm that specializes in providing financial education, coaching, and planning to the Hispanic community. The name of the company is Valemar, which means to prosper. We need a design that is clean, professional, and invokes trust, professionalism, but also welcoming. Our logo is a plant growing from a hand to give the messaging of of being in control of growing your financial future and security. Its part of a larger organization names Celesta Financial Group, who's logo is a tree with multi colored branches. We have the back of the card designed so we just need the front designed. the back is blue, so front needs to be a different background color, not blue.

Target Market(s)

Hispanic Community looking to better their future

Industry/Entity Type

financial services

Contact Information for Business Card

contact info: Anselmo Ibarra Jr, 951-555-0147, info@celestafinancialgroup.example. Celestafinancialgroup.example. tag line: Para un futuro mas seguro!

Requirements
Must have
• basics: logo, contact info.
Nice to have
• possibly incorporate the tree logo provided somehow
Should not have
• should not look like the back, needs to be different from the back provided.

```html
<!DOCTYPE html>
<html lang="es">
<head>
<meta charset="utf-8">
<title>Valemar – tarjeta de presentación</title>
<link rel="stylesheet" href="https://fonts.googleapis.com/css2?family=Montserrat:wght@500;700&family=Roboto:wght@400;500;700&display=swap">
<style>
  :root {
    --backdrop: #dcdcdc;
    --card-red: #b83327;
    --mark-red: #c44236;
    --leaf-green: #6aa843;
    --navy: #012f45;
    --white: #ffffff;
    --leaf-lime: #a6c83a;
    --leaf-blue: #27a4dd;
    --leaf-coral: #e8474c;
    --leaf-lilac: #9f86c0;
    --leaf-gold: #f5c22b;
  }
  * { margin: 0; padding: 0; box-sizing: border-box; }
  html, body {
    width: 1200px; height: 1200px; overflow: hidden;
    background: var(--backdrop);
  }
  .sheet { position: relative; width: 1200px; height: 1200px; }

  /* Front */
  .card-front {
    position: absolute; left: 263px; top: 170px;
    width: 674px; height: 396px;
    background: var(--card-red);
    overflow: hidden;
    font-family: "Roboto", Arial, sans-serif;
  }
  .tagline-band {
    position: absolute; left: 309px; right: 0; top: 332px; height: 32px;
    background: var(--leaf-green);
  }
  .mark-area {
    position: absolute; left: 6px; top: 6px; width: 356px; height: 384px;
    background: var(--mark-red);
    border-radius: 4px;
  }
  .brand-name {
    position: absolute; left: 378px; top: 22px;
    font-family: "Montserrat", sans-serif; font-weight: 500;
    font-size: 56px; line-height: 1; color: var(--leaf-green);
    letter-spacing: -0.5px;
  }
  .brand-sub {
    position: absolute; left: 380px; top: 95px;
    font-family: "Montserrat", sans-serif; font-weight: 700;
    font-size: 15px; letter-spacing: 2.3px; color: var(--white);
  }
  .person-name {
    position: absolute; left: 380px; top: 184px;
    font-weight: 700; font-size: 24px; color: var(--white);
  }
  .person-role {
    position: absolute; left: 380px; top: 214px;
    font-weight: 500; font-size: 17px; color: var(--leaf-green);
  }
  .contact-list {
    position: absolute; left: 380px; top: 251px; list-style: none;
    font-size: 16px; color: var(--white);
  }
  .contact-list li { display: flex; align-items: center; height: 22px; }
  .contact-list svg { width: 11px; height: 11px; margin-right: 5px; flex: none; }
  .tagline {
    position: absolute; left: 380px; top: 337px;
    font-size: 17px; color: var(--card-red);
  }

  /* Back */
  .card-back {
    position: absolute; left: 266px; top: 589px;
    width: 668px; height: 392px;
    background: var(--navy);
    font-family: "Montserrat", sans-serif; color: var(--white);
  }
  .parent-dot {
    position: absolute; left: 72px; top: 68px; width: 140px; height: 140px;
    border-radius: 50%; background: rgba(255,255,255,0.12);
  }
  .divider {
    position: absolute; left: 251px; top: 29px; width: 1.5px; height: 215px;
    background: var(--white);
  }
  .parent-name {
    position: absolute; left: 282px; top: 90px; font-weight: 700; line-height: 1;
  }
  .parent-name .big { display: block; font-size: 84px; letter-spacing: -3px; }
  .parent-name .small { display: block; font-size: 25px; margin-top: 6px; }
  .services {
    position: absolute; left: 0; right: 0; top: 298px;
    text-align: center; font-weight: 500; font-size: 19px; line-height: 26px;
  }
  .services .dot {
    display: inline-block; width: 8px; height: 12px; border-radius: 50%;
    margin: 0 5px 0 8px; vertical-align: -1px;
  }
</style>
</head>
<body>
<div class="sheet">

  <section class="card-front">
    <div class="tagline-band"></div>
    <div class="mark-area" role="img" aria-label="Valemar brand mark: plant growing from an open hand"></div>

    <div class="brand-name">Valemar</div>
    <div class="brand-sub">SERVICIOS FINANCIEROS</div>

    <div class="person-name">Anselmo Ibarra Jr</div>
    <div class="person-role">Founder</div>

    <ul class="contact-list">
      <li>
        <svg viewBox="0 0 12 12"><path fill="#6aa843" d="M2.5 0.8 4.4 3 3.4 4.3c.8 1.8 2.2 3.3 4.2 4.2l1.3-1 2.2 1.9-1.2 1.8C5.3 11.2.8 6.7 1 2z"/></svg>
        951-555-0147
      </li>
      <li>
        <svg viewBox="0 0 12 12"><rect x="0.5" y="2.5" width="11" height="7" fill="none" stroke="#6aa843"/><path d="M0.5 2.5 6 7l5.5-4.5" fill="none" stroke="#6aa843"/></svg>
        info@celestafinancialgroup.example
      </li>
      <li>
        <svg viewBox="0 0 12 12"><g fill="none" stroke="#6aa843" stroke-width="0.9"><circle cx="6" cy="6" r="5"/><ellipse cx="6" cy="6" rx="2.2" ry="5"/><path d="M1 6h10M2 3.5h8M2 8.5h8"/></g></svg>
        Celestafinancialgroup.example
      </li>
    </ul>

    <div class="tagline">Para un futuro mas seguro!</div>
  </section>

  <section class="card-back">
    <div class="parent-dot"></div>
    <div class="divider"></div>
    <div class="parent-name">
      <span class="big">Celesta</span>
      <span class="small">Financial Group Inc</span>
    </div>
    <div class="services">
      <div><span class="dot" style="background:var(--leaf-lime)"></span>Inmigración <span class="dot" style="background:var(--leaf-blue)"></span>Planificacion Financiera</div>
      <div><span class="dot" style="background:var(--leaf-coral)"></span>Seguros <span class="dot" style="background:var(--leaf-lilac)"></span>Impuestos <span class="dot" style="background:var(--leaf-coral)"></span>Y mas</div>
      <div><span class="dot" style="background:var(--leaf-gold)"></span>Preparación de documentos</div>
    </div>
  </section>

</div>
</body>
</html>
```